Amber Lantern Spin Method Needs a Website

I require a Pressline website so that I can do simple edits myself. I want it to be a fairly simple design as the videos and the text will speak for themselves.
The concept is simple, we have developed a revolutionary roulette system that proves the game is NOT random. This breakthrough is absolutely massive. We are offering a 12-part training course to take a beginner to a professional at their own pace through watching videos made by our roulette genius.
Roulette and casinos have a glitzy feel about them and this should be reflected in the style of the site. The roulette wheel, table and chips are very evocative and pictures of these would be good.
There is a home page and 5 other pages containing sub-pages. These should be interlinked and it must be easy to get back to the home page from anywhere on the site.
Tandro links should appear at the bottom of each page.
I really need the site in a hurry as we were let down badly by the last developer we hired who went on holiday and left us in the lurch.

Target Market(s)

Gamblers, betting community, opportunity seekers

Coding

Coded - Design and coding required

Number of Pages Required

1 page

Font styles to use
Sans Serif

Requirements
Must have
• At least two videos on the Home page.
• Tandro details on every page and tab.
• A box for name and email address for interested parties to leave their details.

```html
<!DOCTYPE html>
<html lang="en">
<head>
<meta charset="utf-8">
<title>Our Course – Amber Lantern Spin Method</title>
<link href="https://fonts.googleapis.com/css2?family=Montserrat:wght@400;500;600&display=swap" rel="stylesheet">
<style>
:root{
  --page:#f4f4f4;
  --header:#ffffff;
  --rule:#e4e4e4;
  --ink:#333333;
  --heading:#222222;
  --nav:#555555;
  --player:#8c8c8c;
  --player-dark:#6f6f6f;
  --field:#ffffff;
  --field-line:#cccccc;
  --button:#2b2b2b;
  --footer:#222222;
  --footer-text:#666666;
  --footer-icon:#555555;
}
*{box-sizing:border-box;margin:0;padding:0}
html,body{width:1024px;height:1200px;overflow:hidden}
body{background:var(--page);font-family:"Montserrat",sans-serif;color:var(--ink);position:relative}
.site-header{position:absolute;left:0;top:0;width:1024px;height:43px;background:var(--header);border-bottom:1px solid var(--rule)}
.brand{position:absolute;left:106px;top:10px;display:flex;align-items:center;gap:6px;color:#777;font-size:16px;font-weight:400}
.brand-mark{width:22px;height:22px;border:1.5px solid #777;border-radius:50%}
.main-nav{position:absolute;top:15px;left:0;font-size:9.6px;font-weight:500;color:var(--nav)}
.main-nav span{position:absolute;white-space:nowrap}
.search-icon{position:absolute;left:907px;top:15px}
.section-title{position:absolute;left:0;width:1024px;text-align:center;top:83px;font-size:16px;font-weight:500;color:var(--heading);letter-spacing:1px}
.section-sub{position:absolute;left:0;width:1024px;text-align:center;top:105px;font-size:9px;color:var(--ink);letter-spacing:.3px}
.gallery{position:absolute;left:102px;top:131px;width:820px;height:199px;display:grid;grid-template-columns:repeat(4,1fr);grid-template-rows:repeat(2,1fr)}
.t1{background:linear-gradient(160deg,#1f6b3a,#2c2a22 60%,#8a6a3a)}
.t2{background:linear-gradient(140deg,#8a1414,#b33050 50%,#2a1a3a)}
.t3{background:linear-gradient(120deg,#7a4a28,#1e5a36 55%,#245e3c)}
.t4{background:linear-gradient(150deg,#1e5fb0,#c03030 45%,#1f7040)}
.t5{background:linear-gradient(140deg,#2a3a2a,#1a5e34 55%,#1d6a3a)}
.t6{background:linear-gradient(130deg,#6a4a10,#b88a20 50%,#3a2a10)}
.t7{background:linear-gradient(120deg,#b81818,#4a2a16 35%,#6a3818)}
.t8{background:linear-gradient(150deg,#2a6a40,#1a3a5a 55%,#0d2a4a)}
.post-title{position:absolute;left:102px;top:396px;font-size:16px;font-weight:500;color:var(--heading);letter-spacing:.8px}
.copy{position:absolute;left:102px;width:818px;font-size:9.2px;line-height:12.6px;letter-spacing:.5px;color:var(--ink)}
.player{position:absolute;left:106px;height:13px;width:382px}
.player div{position:absolute;top:0;height:13px;background:var(--player);border-radius:3px}
.player .play{left:0;width:26px}
.player .time{left:30px;width:59px;color:#fff;font-size:6.5px;font-weight:600;line-height:13px;text-align:center;background:var(--player-dark)}
.player .track{left:93px;width:264px}
.player .track::before{content:"";position:absolute;left:7px;top:3px;width:2px;height:7px;background:#ddd}
.player .vol{left:361px;width:20px}
.player svg{position:absolute;left:9px;top:3px}
.signup{position:absolute;left:102px;top:1138px;width:820px;display:flex;align-items:center;gap:8px;font-size:8.5px;letter-spacing:.4px}
.signup-label{font-weight:600;color:var(--heading)}
.signup-field{width:150px;height:18px;background:var(--field);border:1px solid var(--field-line);padding:0 6px;line-height:16px;color:#999}
.signup-button{height:18px;padding:0 12px;background:var(--button);color:#fff;line-height:18px;font-weight:600}
.payment-note{margin-left:auto;color:var(--ink)}
.site-footer{position:absolute;left:0;top:1171px;width:1024px;height:29px;background:var(--footer)}
.credits{position:absolute;left:102px;top:9px;font-size:9px;color:var(--footer-text);letter-spacing:.5px}
.credits b{font-weight:600}
.social{position:absolute;left:777px;top:8px;display:flex;gap:22px}
.social span{width:13px;height:13px;border-radius:50%;background:var(--footer-icon)}
</style>
</head>
<body>
<header class="site-header">
  <div class="brand"><span class="brand-mark"></span>Lantern</div>
  <nav class="main-nav">
    <span style="left:567px">Home</span>
    <span style="left:620px">About</span>
    <span style="left:674px">Services <svg width="6" height="4" viewBox="0 0 6 4"><path d="M.5.5 3 3 5.5.5" fill="none" stroke="#777"/></svg></span>
    <span style="left:754px">Contact</span>
    <span style="left:816px">Login</span>
    <span style="left:866px">Blog</span>
  </nav>
  <svg class="search-icon" width="13" height="13" viewBox="0 0 13 13"><circle cx="7.5" cy="5.5" r="4" fill="none" stroke="#777" stroke-width="1.1"/><path d="M4.6 8.4 1 12" stroke="#777" stroke-width="1.2"/></svg>
</header>

<h1 class="section-title">Our Course</h1>
<p class="section-sub">videos made by our very own roulette genius.</p>

<div class="gallery">
  <div class="t1" role="img" aria-label="Roulette wheel and betting table screenshot"></div>
  <div class="t2" role="img" aria-label="Roulette game win screen"></div>
  <div class="t3" role="img" aria-label="Roulette wheel showing 21 beside the table"></div>
  <div class="t4" role="img" aria-label="Casino games banner with wheel and cards"></div>
  <div class="t5" role="img" aria-label="Roulette wheel with green betting layout"></div>
  <div class="t6" role="img" aria-label="Casino chips and four aces"></div>
  <div class="t7" role="img" aria-label="Roulette wheel with winning result panel"></div>
  <div class="t8" role="img" aria-label="Live roulette table"></div>
</div>

<h2 class="post-title">Lantern Spin at Roulette</h2>
<div class="copy" style="top:420px">
  <p>Introducing the incredible Lantern Spin roulette system. Four years in the making by a roulette genius who has observed hundreds of thousands of spins to create a truly groundbreaking system. Every aspect of the game has been broken down, analysed and rebuilt with a solution. This system questions whether the game of roulette is truly random……and the answer is a resounding NO !!</p>
  <p>The key to success is long term profits but to achieve that you need to look beyond complexity and concentrate on simplicity. The system reverses general logic and considers the number of losses rather than the number of wins. This led to the discovery of the counting system, a perfect, carefully balanced approach to progression that protects your bankroll at all times. This alone would be the perfect complement for any roulette system but when combined with the rules of Lantern Spin, it’s dynamite.</p>
</div>

<div class="player" style="top:652px">
  <div class="play"><svg width="8" height="7" viewBox="0 0 8 7"><path d="M0 0 8 3.5 0 7z" fill="#ddd"/></svg></div>
  <div class="time">00:00 / 00:00</div>
  <div class="track"></div>
  <div class="vol"><svg width="6" height="7" viewBox="0 0 6 7" style="left:7px"><path d="M6 0 0 3.5 6 7z" fill="#ddd"/></svg></div>
</div>

<div class="copy" style="top:696px">
  <p>The second major breakthrough was the discovery of the families. These are groups of numbers that appear regularly within a few spins of each other. For students learning the system, this is their first ‘wow’ moment. The regularity of hits between numbers in the families is staggering and underpins the whole system.</p>
  <p>Finally, the families were analysed further and broken down into pairs. This provided the opportunity to shorten the average playing time of each session to around half an hour. The philosophy of Lantern Spin is to build your stakes slowly and then when everything falls into place, make a big win and walk away.</p>
  <p style="margin-top:8px">Watch this video and prepare to be amazed</p>
</div>

<div class="player" style="top:935px">
  <div class="play"><svg width="8" height="7" viewBox="0 0 8 7"><path d="M0 0 8 3.5 0 7z" fill="#ddd"/></svg></div>
  <div class="time">00:00 / 00:00</div>
  <div class="track"></div>
  <div class="vol"><svg width="6" height="7" viewBox="0 0 6 7" style="left:7px"><path d="M6 0 0 3.5 6 7z" fill="#ddd"/></svg></div>
</div>

<div class="copy" style="top:979px">
  <p>We are offering a unique opportunity to learn the Lantern Spin system through a series of videos made by our very own roulette genius. You will learn every aspect of this amazing system at your own pace, only moving on to the next stage when you have totally mastered the previous step. We encourage our students to practise their skills in play mode and when they are completely confident and winning every session, play with real money. This allows them to build their bankroll and pay for each video as they go along.</p>
  <p>Our course has been designed to make each step easy to learn and understand. Each video leads into the next and builds a new layer of understanding on top of the last. Committing the information to memory is very easy using this method and our students become experts at analysing everything unfolding before them in a roulette session.</p>
  <p>Some of our students become professional players, enjoying the thrills of playing in bricks and mortar casinos around the world. Others are happy to play part-time from home and build a second income. The fact is that once you have the skills to be successful at roulette, the options really are endless.</p>
  <p>We are only successful if our students achieve their goals. We provide individual coaching sessions if anyone needs extra tuition and will always endeavor to answer</p>
</div>

<form class="signup">
  <span class="signup-label">Stay in touch</span>
  <span class="signup-field">Name</span>
  <span class="signup-field">Email address</span>
  <span class="signup-button">Join</span>
  <span class="payment-note">Secure payments for each video by Tandro</span>
</form>

<footer class="site-footer">
  <p class="credits">Designed by <b>Harbor Themes</b> | Powered by <b>Pressline</b></p>
  <div class="social"><span></span><span></span><span></span><span></span></div>
</footer>
</body>
</html>
```